Bright Harbor Property Institute

This must be done in word press and I will need about 7 tabs The home page, Information page, Schedule and Cost page which will link to a Email me form, a online registration a about us and location/contact tab Each tab will then open several other pages. The home page will describe different courses that we offer since all the schools are about the same you can get a good ideal by going to plomvex.example or keelwardhomeclasses.example and looking at their site I would like mine to be similar as the courses are exactly the same but I would like the site to be more modern I also need it to be in word press so I can change it and update the dates as they change I have attached he logo below

Target Market(s)

people interested in getting into real estate and those who need continuing education

Coding

Number of Pages Required

Font styles to use
Sans Serif

Colors
3276b5

Requirements
Must have
• A page to schedule classes, a tab so the college I am partnering with can link the online courses to the back side, a page that describes the type of classes I offer

```html
<!DOCTYPE html>
<html lang="en">
<head>
<meta charset="utf-8">
<title>Bright Harbor Property Institute</title>
<link rel="stylesheet" href="https://fonts.googleapis.com/css2?family=Roboto:wght@300;400;500;700&family=Libre+Baskerville:wght@700&display=swap">
<style>
:root{
  --blue:#4169b3;
  --blue-dark:#3a5fa3;
  --ink:#222;
  --text:#555;
  --dark:#3b3b3b;
  --nav-active:#3a3a3a;
  --footer:#5a5a5a;
  --grey-bg:#ebebeb;
  --white:#fff;
}
*{box-sizing:border-box;margin:0;padding:0}
html,body{width:1200px;height:2899px;overflow:hidden}
body{font-family:"Roboto",sans-serif;color:var(--text);background:var(--white);position:relative}
/* header */
.topbar{position:absolute;left:0;top:0;width:1200px;height:68px;background:var(--white)}
.contact-item{position:absolute;display:flex;align-items:center;gap:14px;color:var(--text)}
.icon-ring{width:30px;height:30px;border:1.5px solid var(--blue);border-radius:50%;display:flex;align-items:center;justify-content:center}
.brand{position:absolute;left:500px;top:20px;display:flex;align-items:center;gap:8px;font-family:"Roboto",sans-serif;font-weight:700;font-size:21px;color:var(--blue)}
.brand-dot{width:14px;height:14px;border-radius:50%;background:var(--blue)}
.cart{position:absolute;left:1028px;top:20px}
.cart-count{position:absolute;left:1047px;top:15px;width:14px;height:14px;border:1px solid var(--blue);border-radius:50%;font-size:10px;line-height:12px;text-align:center;color:var(--blue)}
.mainnav{position:absolute;left:0;top:68px;width:1200px;height:38px;background:var(--blue);display:flex;padding-left:111px}
.mainnav a{color:var(--white);text-decoration:none;font-size:16px;line-height:38px;padding:0 15px;margin-right:10px}
.mainnav a.active{background:var(--nav-active)}
/* hero */
.hero{position:absolute;left:0;top:106px;width:1200px;height:562px;background:linear-gradient(90deg,#7d8a6a 0%,#b59a6a 40%,#c8a877 65%,#d6b98c 100%)}
.hero-title{position:absolute;left:530px;top:122px;width:620px;text-align:center;font-family:"Libre Baskerville",serif;font-size:50px;line-height:60px;color:var(--white);text-shadow:0 2px 6px rgba(0,0,0,.35)}
.btn{display:inline-flex;align-items:center;gap:9px;font-weight:500;font-size:17px;text-transform:uppercase;text-decoration:none}
.btn-solid{background:var(--blue);color:var(--white);padding:0 16px;height:50px}
.hero .btn-solid{position:absolute;left:759px;top:345px}
.dots{position:absolute;left:795px;top:424px;display:flex;gap:5px}
.dots span{width:14px;height:14px;border-radius:50%;background:var(--blue)}
.dots span.on{background:var(--white);border:3px solid var(--blue)}
/* about */
.section-title{font-family:"Libre Baskerville",serif;font-size:38px;color:var(--ink)}
.about-title{position:absolute;left:113px;top:728px}
.about-title span{color:var(--blue)}
.about-text{position:absolute;left:113px;top:778px;width:455px;font-size:16px;line-height:26px;font-weight:300;color:#555}
.about .btn-solid{position:absolute;left:114px;top:952px;height:50px}
.about-photo{position:absolute;left:658px;top:745px;width:428px;height:270px;border:4px solid var(--white);box-shadow:0 0 8px rgba(0,0,0,.3);background:linear-gradient(120deg,#c9d9e8,#e9e4df 50%,#9aa6b5)}
/* services */
.feature{position:absolute;width:330px;height:114px;border-radius:60px;background:var(--white);box-shadow:0 3px 10px rgba(0,0,0,.12)}
.feature .disc{position:absolute;top:10px;width:98px;height:98px;border-radius:50%;display:flex;align-items:center;justify-content:center}
.disc.blue{background:var(--blue)}
.disc.dark{background:var(--dark)}
.feature.left .disc{right:12px}
.feature.right .disc{left:12px}
.feature h3{font-size:19px;font-weight:500;color:#111;margin-top:20px;white-space:nowrap}
.feature p{font-size:16px;line-height:26px;font-weight:300;color:#555;margin-top:4px}
.feature.left .copy{position:absolute;right:125px;text-align:right;width:210px}
.feature.right .copy{position:absolute;left:128px;width:200px}
.feature h3.long{font-size:18px}
.center-brand{position:absolute;left:478px;top:1260px;width:232px;display:flex;align-items:center;justify-content:center;gap:8px;font-weight:700;font-size:24px;color:var(--blue)}
/* courses */
.courses{position:absolute;left:0;top:1545px;width:1200px;height:498px;background:var(--grey-bg)}
.courses .section-title{position:absolute;left:0;top:48px;width:1200px;text-align:center}
.course{position:absolute;top:140px;width:480px;height:273px;color:var(--white);text-align:center}
.course.blue{left:110px;background:var(--blue)}
.course.dark{left:608px;background:var(--dark)}
.course h3{font-size:23px;font-weight:500;line-height:30px;text-transform:uppercase;position:absolute;left:0;width:100%}
.course .price{position:absolute;top:108px;width:100%;font-size:30px;font-weight:500}
.course .per{position:absolute;top:150px;width:100%;font-size:13px}
.course .tag{position:absolute;top:183px;width:100%;font-size:20px;font-weight:300}
.btn-outline{position:absolute;top:248px;left:157px;height:48px;padding:0 18px;background:var(--white);color:var(--blue);border:2px solid var(--blue)}
/* testimonials */
.testimonials .section-title{position:absolute;left:0;top:2085px;width:1200px;text-align:center}
.quote-back{position:absolute;left:193px;top:2228px;width:815px;height:180px;background:var(--white);box-shadow:0 0 10px rgba(0,0,0,.1)}
.quote-card{position:absolute;left:228px;top:2193px;width:744px;height:251px;background:var(--white);box-shadow:0 0 10px rgba(0,0,0,.12);text-align:center}
.quote-mark{position:absolute;left:576px;top:2171px;width:48px;height:48px;border-radius:50%;border:2px solid var(--blue);background:var(--white);display:flex;align-items:center;justify-content:center}
.quote-card p{margin:50px 60px 0;font-size:15.5px;line-height:26px;font-weight:300;color:#555}
.quote-rule{width:72px;height:2px;background:var(--blue);margin:10px auto 0}
.quote-author{margin-top:18px;font-size:16px;color:#111;font-weight:500}
.quote-author span{font-weight:300;color:#666;font-size:15px}
.arrow{position:absolute;top:2467px;width:30px;height:30px;border-radius:50%;background:var(--blue);display:flex;align-items:center;justify-content:center}
/* footer */
.footer{position:absolute;left:0;top:2555px;width:1200px;height:295px;background:var(--footer)}
.foot-col{position:absolute;top:58px;color:var(--white)}
.foot-col h4{font-size:18px;font-weight:500;text-decoration:underline;text-underline-offset:4px;margin-bottom:12px}
.foot-col li{list-style:none;font-size:17px;line-height:35.5px;font-weight:300}
.foot-col li::before{content:"»";margin-right:16px;font-weight:500}
.bottombar{position:absolute;left:0;top:2850px;width:1200px;height:49px;background:var(--blue);color:var(--white)}
.copyright{position:absolute;left:115px;top:15px;font-size:16px}
.social{position:absolute;left:1012px;top:13px;display:flex;gap:12px}
.social span{width:22px;height:22px;border:2px solid var(--white);border-radius:50%}
</style>
</head>
<body>

<header class="topbar">
  <div class="contact-item" style="left:131px;top:18px;font-size:15px">
    <span class="icon-ring"><svg width="14" height="11" viewBox="0 0 14 11" fill="none" stroke="#4169b3" stroke-width="1.4"><rect x="1" y="1" width="12" height="9" rx="1"/><path d="M1 2l6 4 6-4"/></svg></span>
    info@brightharborinstitute.example
  </div>
  <div class="brand"><span class="brand-dot"></span>Bright Harbor</div>
  <div class="contact-item" style="left:781px;top:18px;font-size:21px;font-weight:500">
    <span class="icon-ring"><svg width="14" height="14" viewBox="0 0 24 24" fill="none" stroke="#4169b3" stroke-width="2"><path d="M5 3h4l2 5-3 2a12 12 0 006 6l2-3 5 2v4a2 2 0 01-2 2A18 18 0 013 5a2 2 0 012-2z"/></svg></span>
    555 014 2290
  </div>
  <svg class="cart" width="20" height="18" viewBox="0 0 20 18" fill="#4169b3"><path d="M5 3h15l-2.5 8H7z"/><circle cx="8" cy="15" r="2"/><circle cx="16" cy="15" r="2"/></svg>
  <div class="cart-count">0</div>
</header>

<nav class="mainnav">
  <a class="active" href="#">HOME</a><a href="#">INFORMATION</a><a href="#">SCHEDULE &amp; COST</a><a href="#">REGISTRATION</a><a href="#">ONLINE COURSES</a><a href="#">ADVANTAGE</a><a href="#">CONTACT</a>
</nav>

<section class="hero" role="img" aria-label="Photo of a smiling student holding books outdoors in warm sunlight">
  <h1 class="hero-title">BRIGHT HARBOR<br>PROPERTY<br>INSTITUTE</h1>
  <a class="btn btn-solid" href="#">Get Started <svg width="16" height="16" viewBox="0 0 16 16"><circle cx="8" cy="8" r="8" fill="#fff"/><path d="M6 4l4 4-4 4" stroke="#4169b3" stroke-width="2" fill="none"/></svg></a>
  <div class="dots"><span></span><span></span><span class="on"></span><span></span><span></span></div>
</section>

<section class="about">
  <h2 class="section-title about-title"><span>ABOUT</span> US</h2>
  <p class="about-text">Lorem ipsum dolor sit amet, consectetur adipiscing elit, sed do eiusmod tempor incididunt ut labore et dolore magna aliqua. Ut enim ad minim veniam, quis nostrud exercitation ullamco laboris nisi ut aliquip ex ea commodo consequat. Duis aute irure dolor in reprehenderit in voluptate velit esse cillum dolore eu fugiat nulla pariatur. Excepteur sint occaecat cupidatat.</p>
  <a class="btn btn-solid" href="#">Read More <svg width="16" height="16" viewBox="0 0 16 16"><circle cx="8" cy="8" r="8" fill="#fff"/><path d="M6 4l4 4-4 4" stroke="#4169b3" stroke-width="2" fill="none"/></svg></a>
  <div class="about-photo" role="img" aria-label="Photo of students working on laptops in a bright classroom"></div>
</section>

<section class="services">
  <div class="feature left" style="left:133px;top:1082px">
    <div class="copy"><h3>INFORMATION</h3><p>Lorem ipsum dolor sit amet, consectetur adipiscing.</p></div>
    <div class="disc blue"><svg width="40" height="50" viewBox="0 0 40 50" fill="none" stroke="#fff" stroke-width="2.5"><path d="M20 47S4 28 4 18a16 16 0 0132 0c0 10-16 29-16 29z"/><circle cx="20" cy="18" r="6"/></svg></div>
  </div>
  <div class="feature left" style="left:133px;top:1226px">
    <div class="copy"><h3>SCHEDULE &amp; COST</h3><p>Lorem ipsum dolor sit amet, consectetur adipiscing.</p></div>
    <div class="disc dark"><svg width="50" height="50" viewBox="0 0 50 50" fill="none" stroke="#fff" stroke-width="2.2"><path d="M16 10h12l-3 6h-6z"/><path d="M19 16C8 24 8 42 22 42s14-18 3-26"/><text x="16" y="36" font-size="14" fill="#fff" stroke="none" font-family="Roboto,sans-serif" font-weight="700">$</text><rect x="30" y="26" width="14" height="5"/><rect x="30" y="31" width="14" height="5"/><rect x="30" y="36" width="14" height="5"/></svg></div>
  </div>
  <div class="feature left" style="left:133px;top:1371px">
    <div class="copy"><h3>REGISTRATION</h3><p>Lorem ipsum dolor sit amet, consectetur adipiscing.</p></div>
    <div class="disc blue"><svg width="50" height="50" viewBox="0 0 50 50" fill="none" stroke="#fff" stroke-width="2.2"><rect x="8" y="8" width="30" height="36" rx="2"/><path d="M13 16h8M13 22h18M13 28h16M13 34h12"/><path d="M44 14L30 38l-3 3 1-4 14-24z"/></svg></div>
  </div>

  <div class="feature right" style="left:733px;top:1082px">
    <div class="disc dark"><svg width="52" height="48" viewBox="0 0 52 48" fill="none" stroke="#fff" stroke-width="2.2"><rect x="4" y="4" width="44" height="30" rx="2"/><path d="M20 34v7M32 34v7M14 43h24"/><path d="M16 17l10-5 10 5-10 5z"/><path d="M20 19v5c4 3 8 3 12 0v-5"/></svg></div>
    <div class="copy"><h3>ONLINE COURSES</h3><p>Lorem ipsum dolor sit amet, consectetur adipiscing.</p></div>
  </div>
  <div class="feature right" style="left:733px;top:1226px">
    <div class="disc blue"><svg width="56" height="56" viewBox="0 0 56 56" fill="none" stroke="#fff" stroke-width="3"><circle cx="28" cy="28" r="25"/><path d="M20 22a8 8 0 1112 7c-3 2-4 3-4 7"/><circle cx="28" cy="42" r="1.5" fill="#fff"/></svg></div>
    <div class="copy"><h3 class="long">WHY BRIGHT HARBOR ?</h3><p>Lorem ipsum dolor sit amet, consectetur adipiscing.</p></div>
  </div>
  <div class="feature right" style="left:733px;top:1371px">
    <div class="disc dark"><svg width="44" height="54" viewBox="0 0 44 54" fill="none" stroke="#fff" stroke-width="2.2"><path d="M18 30V12a3 3 0 016 0v14l9 2c3 1 4 3 4 6l-2 12c-1 3-3 5-6 5H21c-2 0-4-1-5-3l-7-11c-1-2 1-4 3-3l6 5"/><path d="M12 16a9 9 0 1118 0"/></svg></div>
    <div class="copy"><h3>GET IN TOUCH</h3><p>Lorem ipsum dolor sit amet, consectetur adipiscing.</p></div>
  </div>

  <div class="center-brand"><span class="brand-dot" style="width:16px;height:16px"></span>Bright Harbor</div>
</section>

<section class="courses">
  <h2 class="section-title">ONLINE COURSES</h2>
  <article class="course blue">
    <h3 style="top:36px">The Tennessee Real Estate<br>Principles Course</h3>
    <div class="price">$360.00</div>
    <div class="per">Per month</div>
    <div class="tag">Quis autem / vel eum</div>
    <a class="btn btn-outline" href="#">Read More <svg width="16" height="16" viewBox="0 0 16 16"><circle cx="8" cy="8" r="8" fill="#4169b3"/><path d="M6 4l4 4-4 4" stroke="#fff" stroke-width="2" fill="none"/></svg></a>
  </article>
  <article class="course dark">
    <h3 style="top:50px">New Affiliates Course</h3>
    <div class="price">$165.00</div>
    <div class="per">Per month</div>
    <div class="tag">Quis autem / vel eum</div>
    <a class="btn btn-outline" href="#">Read More <svg width="16" height="16" viewBox="0 0 16 16"><circle cx="8" cy="8" r="8" fill="#4169b3"/><path d="M6 4l4 4-4 4" stroke="#fff" stroke-width="2" fill="none"/></svg></a>
  </article>
</section>

<section class="testimonials">
  <h2 class="section-title">TESTIMONIALS</h2>
  <div class="quote-back"></div>
  <div class="quote-card">
    <p>Sed ut perspiciatis unde omnis iste natus error sit voluptatem accusantium doloremque laudantium, totam rem aperiam, eaque ipsa quae ab illo inventore veritatis et quasi architecto beatae vitae dicta sunt explicabo. Nemo enim ipsam voluptatem quia voluptas sit aspernatur aut odit aut fugit, sed quia consequuntur magni dolores eos qui ratione voluptatem sequi nesciunt.</p>
    <div class="quote-rule"></div>
    <div class="quote-author">DANA WHITFIELD , <span>Businessman</span></div>
  </div>
  <div class="quote-mark"><svg width="24" height="18" viewBox="0 0 24 18" fill="#4169b3"><path d="M1 10a8 8 0 018-9v3a5 5 0 00-4 4h4v9H1z"/><path d="M13 10a8 8 0 018-9v3a5 5 0 00-4 4h4v9h-8z"/></svg></div>
  <div class="arrow" style="left:565px"><svg width="10" height="12" viewBox="0 0 10 12"><path d="M7 1L2 6l5 5" stroke="#fff" stroke-width="2" fill="none"/></svg></div>
  <div class="arrow" style="left:605px"><svg width="10" height="12" viewBox="0 0 10 12"><path d="M3 1l5 5-5 5" stroke="#fff" stroke-width="2" fill="none"/></svg></div>
</section>

<footer class="footer">
  <div class="foot-col" style="left:123px"><h4>QUICK LINKS</h4><ul><li>Home</li><li>About Us</li><li>Online Courses</li><li>Latest blog</li><li>Reviews</li></ul></div>
  <div class="foot-col" style="left:368px"><h4>OTHER LINKS</h4><ul><li>FAQ</li><li>Privacy Policy</li><li>Reviews</li><li>Help</li><li>Terms &amp; Conditions</li></ul></div>
  <div class="foot-col" style="left:653px"><h4>LOREM IPSUM</h4><ul><li>Excepteur sint</li><li>Quis autem vel</li><li>Et harum quidem</li><li>Itaque earum</li></ul></div>
  <div class="foot-col" style="left:927px"><h4>VOLUPTATE VELIT</h4><ul><li>Minima veniam</li><li>Exercitationem</li><li>Corporis suscipit</li><li>Nemo enim</li><li>Neque porro</li></ul></div>
</footer>

<div class="bottombar">
  <div class="copyright">© 2019 Bright Harbor Property Institute. All Rights Reserved</div>
  <div class="social" aria-label="Social links"><span></span><span></span></div>
</div>

</body>
</html>
```